CRPG is needing business cards, and stationary created.

Pixel Forge created a logo for our business, and now we are wanting business cards, and stationary. I have included two designs of the same logo. Please feel free to use them as you want. The name of the company is Cedar Ridge Property Group LLC, the address is 812 NE Willow Ln., Suite 9, the city & state is Bend, Oregon, zip code is 97815, Telephone number is 541-327-4489, Fax number is 541-327-6051, the name on the business card is Carl Whitby CMCA

Industry/Entity Type

Property Management

Contact Information for Business Card

The card needs to look professional. Upscale.

Requirements
Must have
• The colors we are using are on the logo that has been uploaded.

```html
<!DOCTYPE html>
<html lang="en">
<head>
<meta charset="utf-8">
<title>Cedar Ridge Property Group — Business Card</title>
<link href="https://fonts.googleapis.com/css2?family=Nanum+Gothic:wght@400;700;800&display=swap" rel="stylesheet">
<style>
  :root {
    --backdrop: #6b6b6b;
    --green: #4f8e79;
    --green-light: #62998a;
    --green-deep: #3f7a68;
    --slate: #4a5465;
    --slate-deep: #363d4b;
    --ink: #2f3644;
    --paper: #f2f2f0;
    --muted: #d9dde3;
  }
  * { box-sizing: border-box; margin: 0; padding: 0; }
  html, body {
    width: 1200px; height: 800px; overflow: hidden;
    background: var(--backdrop);
    font-family: "Nanum Gothic", sans-serif;
  }
  .sheet {
    width: 1200px; height: 800px;
    display: flex; align-items: center; justify-content: center; gap: 40px;
  }
  .card {
    position: relative; width: 540px; height: 309px; overflow: hidden;
    box-shadow: 0 10px 30px rgba(0,0,0,.25);
  }

  /* Front */
  .card-front {
    background: linear-gradient(115deg, var(--green-light) 0%, var(--green) 55%, var(--green-deep) 100%);
  }
  .card-front .beam { position: absolute; inset: 0; }
  .front-brand {
    position: absolute; left: 0; right: 0; top: 96px;
    display: flex; flex-direction: column; align-items: center; gap: 12px;
  }
  .brand-square {
    width: 44px; height: 44px; background: var(--ink);
  }
  .brand-name {
    font-weight: 800; font-size: 26px; letter-spacing: 1px; color: var(--ink);
  }
  .front-company {
    position: absolute; left: 0; right: 0; bottom: 22px; text-align: center;
    font-size: 11px; color: var(--ink); letter-spacing: .4px;
  }

  /* Back */
  .card-back {
    background: radial-gradient(ellipse at 30% 25%, var(--slate) 0%, var(--slate) 40%, var(--slate-deep) 100%);
    color: var(--muted);
  }
  .card-back .beam { position: absolute; inset: 0; }
  .back-brand {
    position: absolute; left: 44px; top: 78px;
    display: flex; flex-direction: column; align-items: flex-start; gap: 10px;
  }
  .back-brand .brand-square { width: 36px; height: 36px; background: var(--paper); }
  .back-brand .brand-name { color: var(--paper); font-size: 28px; }
  .back-brand .brand-rule { width: 190px; height: 1px; background: var(--green-light); }
  .divider {
    position: absolute; left: 262px; top: 70px; width: 1px; height: 190px;
    background: linear-gradient(to bottom, rgba(98,153,138,0) 0%, var(--green-light) 40%, rgba(98,153,138,0) 100%);
  }
  .contact { position: absolute; left: 282px; top: 76px; right: 18px; }
  .contact-name { font-size: 19px; color: var(--paper); margin-bottom: 30px; }
  .contact-name .cred { color: var(--green-light); margin-left: 4px; }
  .contact p { font-size: 9.5px; line-height: 1.55; color: var(--muted); }
  .contact .lines { margin-bottom: 20px; }
</style>
</head>
<body>
<main class="sheet">
  <section class="card card-front" aria-label="Business card front">
    <svg class="beam" width="540" height="309" viewBox="0 0 540 309" aria-hidden="true">
      <defs>
        <linearGradient id="frontBeam" x1="1" y1="0" x2="0" y2="1">
          <stop offset="0" stop-color="#2f3644" stop-opacity=".22"/>
          <stop offset="1" stop-color="#2f3644" stop-opacity="0"/>
        </linearGradient>
      </defs>
      <polygon points="250,100 290,150 150,309 0,309 0,180" fill="url(#frontBeam)"/>
    </svg>
    <div class="front-brand">
      <span class="brand-square"></span>
      <span class="brand-name">CEDAR RIDGE</span>
    </div>
    <p class="front-company">Cedar Ridge Property Group LLC</p>
  </section>

  <section class="card card-back" aria-label="Business card back">
    <svg class="beam" width="540" height="309" viewBox="0 0 540 309" aria-hidden="true">
      <defs>
        <linearGradient id="backBeam" x1="1" y1="0" x2="0" y2="1">
          <stop offset="0" stop-color="#4f8e79" stop-opacity=".35"/>
          <stop offset="1" stop-color="#4f8e79" stop-opacity="0"/>
        </linearGradient>
      </defs>
      <polygon points="80,78 120,100 60,260 0,260 0,170" fill="url(#backBeam)"/>
    </svg>
    <div class="back-brand">
      <span class="brand-square"></span>
      <span class="brand-name">CEDAR RIDGE</span>
      <span class="brand-rule"></span>
    </div>
    <div class="divider"></div>
    <div class="contact">
      <h1 class="contact-name">Carl Whitby<span class="cred">CMCA</span></h1>
      <p class="lines">Cedar Ridge Property Group LLC,<br>
        812 NE Willow Ln., Suite 9, the city &amp; state is Bend,<br>
        Oregon, zip code 97815</p>
      <p>Telephone: 541-327-4489<br>Fax: 541-327-6051</p>
    </div>
  </section>
</main>
</body>
</html>
```